I would like to modify/update my 2 step login screen

I want a more modern looking login page for our document imaging application. I need to keep all of the same elements and buttons that currently exist. The first 2 screens are the login. The 3rd is a screenshot of the actual application home page.

```html
<!DOCTYPE html>
<html lang="en">
<head>
<meta charset="UTF-8">
<title>NLS Login</title>
<link href="https://fonts.googleapis.com/css2?family=Open+Sans:wght@400;600;700&display=swap" rel="stylesheet">
<style>
  :root {
    --page-bg: #d4ebd5;
    --card-bg: #ffffff;
    --ink: #111111;
    --muted: #6f6f6f;
    --field-border: #8a8a8a;
    --primary: #5cb85c;
    --signup: #2f6534;
    --art-light: #9fd29f;
    --art-mid: #b9dcb9;
  }
  * { box-sizing: border-box; margin: 0; padding: 0; }
  html, body { width: 1200px; height: 675px; overflow: hidden; }
  body {
    position: relative;
    background: var(--page-bg);
    font-family: "Open Sans", sans-serif;
    color: var(--ink);
  }
  .brand {
    position: absolute; left: 100px; top: 40px;
    display: flex; align-items: center; gap: 8px;
    font-weight: 700; font-size: 17px; line-height: 1.1; color: var(--ink);
  }
  .brand-mark { width: 30px; height: 30px; background: var(--ink); }
  .signup-btn {
    position: absolute; left: 1031px; top: 44px; width: 69px; height: 27px;
    background: var(--signup); color: #fff; border: 0; border-radius: 2px;
    font-family: "Open Sans", sans-serif; font-weight: 600; font-size: 13px;
  }
  .art {
    position: absolute; border-radius: 50%;
  }
  .art-desk {
    left: 91px; top: 253px; width: 266px; height: 247px;
    background: radial-gradient(ellipse at 55% 60%, var(--art-light), rgba(159,210,159,0) 70%);
  }
  .art-meeting {
    left: 847px; top: 228px; width: 250px; height: 231px;
    background: radial-gradient(ellipse at 50% 65%, var(--art-mid), rgba(185,220,185,0) 70%);
  }
  .login-card {
    position: absolute; left: 381px; top: 111px; width: 437px; height: 452px;
    background: var(--card-bg); border-radius: 12px;
    box-shadow: 0 4px 14px rgba(0,0,0,0.06);
    text-align: center;
  }
  .login-title { position: absolute; top: 45px; width: 100%; font-size: 25px; font-weight: 600; }
  .login-subtitle { position: absolute; top: 89px; width: 100%; font-size: 15.5px; font-weight: 400; }
  .field {
    position: absolute; left: 25px; width: 388px; height: 41px;
    border: 1px solid var(--field-border); border-radius: 4px;
    padding-left: 20px; font-family: "Open Sans", sans-serif; font-size: 13px; color: var(--ink);
    background: #fff;
  }
  .field::placeholder { color: var(--muted); }
  .field-username { top: 153px; }
  .field-password { top: 212px; }
  .login-btn {
    position: absolute; left: 25px; top: 286px; width: 388px; height: 41px;
    background: var(--primary); color: #fff; border: 0; border-radius: 4px;
    font-family: "Open Sans", sans-serif; font-weight: 700; font-size: 16px;
    white-space: pre;
  }
  .reset-line { position: absolute; top: 392px; width: 100%; font-size: 13px; color: #444; }
  .reset-line a { color: #333; font-weight: 600; text-decoration: none; }
</style>
</head>
<body>
  <div class="brand"><span class="brand-mark"></span><span>Northline<br>Systems</span></div>
  <button class="signup-btn">Sign up</button>

  <div class="art art-desk" role="img" aria-label="Illustration of a woman with headphones working at a laptop and drawing tablet, with a cat on the desk"></div>
  <div class="art art-meeting" role="img" aria-label="Illustration of two colleagues talking at a round table with a laptop, coffee cup and briefcases"></div>

  <main class="login-card">
    <h1 class="login-title">NLS Login</h1>
    <p class="login-subtitle">Hey! Enter Your Detail To Get Login</p>
    <input class="field field-username" type="text" placeholder="Username">
    <input class="field field-password" type="password" placeholder="Password">
    <button class="login-btn">Login  to NLSDEMO23</button>
    <p class="reset-line">Forget Password? <a href="#">Reset now</a></p>
  </main>
</body>
</html>
```